Web Design / SEO Business Needs a Custom Wordpress Design

- The custom wordpress design is for a new web design / seo company based in Montreal.
- We need approx. 15 page website
- The wordpress design must be custom made
- Main colors are blue and white (try to use white background)
- The main features of my requirements can be found on competitor website, nice look feel/functionality : http://quillmarshstudio.us (but use different colors)
- content will be provided by us
- We will be providing services such as Web design, SEO, Hosting, and Social Media.
- I want the homepage slider and the homepage content to be identical to : http://brambleforge.com/ (we will modify later) (use different colors)
-

Target Market(s)

Businesses or individuals looking for high quality Web design and Services. Male and females from 18-65 age.

Requirements
Must have
• - 15 pages
- Home page slider
- Integrated Blog
- Comparison tables of services offered
- Site Search
- Smartphone compatibility
- Email Optin Form / Newsletter on home page
- Request Quote page
- Contact Form
- SEO Section must be identical to :http://brambleforge.com/payment/seo (use different colors)
- Web Design must be identical to :http://brambleforge.com/payment/index (use different colors)
- very nice images related to content (selected by you)
- Social media logos
Nice to have
• -User friendly tour of website using slider
- nice good quality photos relevant to website
- Live Support
- Simple tables for for price comparison between the various packages we have to offer ... example: Basic Package etc. Example : http://quillmarshstudio.us/payment/seo
- Portfolio carousel , and capability to easily add more web design examples that we have to our portfolio.
- Nice easy to read fonts
- Membership Site

```html
<!DOCTYPE html>
<html lang="en">
<head>
<meta charset="utf-8">
<title>Corvane Web Solutions</title>
<link rel="stylesheet" href="https://fonts.googleapis.com/css2?family=PT+Sans:wght@400;700&family=Arimo:ital,wght@0,400;0,700;1,400&display=swap">
<style>
:root{
  --blue:#2e8ae6;
  --blue-dark:#1f6fc0;
  --paper:#f1f1f1;
  --ink:#333;
  --muted:#888;
  --teal:#2d5f73;
  --night:#161616;
  --night-2:#222;
  --gold:#f5a800;
  --gold-bright:#fdc42a;
  --slate:#8fa7b0;
}
*{box-sizing:border-box;margin:0;padding:0}
html,body{width:769px;height:1200px;overflow:hidden}
body{position:relative;background:var(--paper);font-family:"Arimo",Arial,sans-serif;font-size:7px;color:var(--ink)}
.abs{position:absolute}
h2,h3,.heading{font-family:"PT Sans",Arial,sans-serif;font-weight:400}

/* top bar */
.topbar{left:112px;top:5px;font-size:6.5px;color:var(--muted);font-style:italic}
.topbar a{color:var(--blue);text-decoration:none}
.social{top:3px;left:580px;display:flex;gap:7px}
.social span{width:10px;height:10px;border-radius:2px;border:1px solid #b5b5b5}
.social span:last-child,.social span:nth-child(4){border-radius:50%}

/* header */
.brand{left:110px;top:32px;display:flex;align-items:center;gap:6px}
.brand-name{font-family:"PT Sans",Arial,sans-serif;font-weight:700;font-size:24px;color:var(--blue)}
.brand-mark{width:14px;height:14px;border-radius:50%;background:var(--blue)}
.brand-tag{left:136px;top:58px;font-size:8px;letter-spacing:1px;color:#9ab}
.nav{top:35px;left:405px;display:flex;align-items:center;font-size:8px;color:#666}
.nav a{text-decoration:none;color:#666;margin-right:28px}
.nav .current{background:var(--blue);color:#fff;padding:4px 12px;border-radius:2px;margin-right:18px;border:1px solid var(--blue-dark)}
.nav .open{color:var(--blue)}
.dropdown{left:577px;top:56px;width:108px;height:93px;background:#f7f7f7;border-top:2px solid var(--blue);box-shadow:0 1px 3px rgba(0,0,0,.25);padding:10px 8px 0 11px}
.dropdown li{list-style:none;font-size:6.5px;color:#666;height:18px;border-bottom:1px solid #ddd;padding-top:4px}
.dropdown li::before{content:"› ";color:#999}
.dropdown .active{color:var(--blue)}

/* slider */
.rule{left:0;width:769px;height:2px;background:var(--blue)}
.slider-band{left:0;top:86px;width:769px;height:249px;background:#e6e6e6}
.slide-image{left:100px;top:86px;width:570px;height:248px;background:linear-gradient(#c9c9c9,#c2c2c2);border:1px solid #aaa}
.arrow-big{top:196px;width:34px;height:36px;background:var(--blue);border:2px solid #1a67b5;display:flex;align-items:center;justify-content:center}
.arrow-big.left{left:69px;border-radius:18px 4px 4px 18px}
.arrow-big.right{left:668px;border-radius:4px 18px 18px 4px}
.caption{left:237px;top:228px;width:420px;height:96px;background:#3e3e3e;border-top:3px solid var(--blue);padding:10px 13px;color:#fff}
.caption h2{color:var(--gold);font-size:13px;margin-bottom:8px}
.caption p{font-size:6.6px;line-height:1.65}
.cta{display:flex;align-items:center;gap:7px;margin-top:7px;font-size:10px}
.btn-blue{background:var(--blue);font-family:"PT Sans",Arial,sans-serif;font-weight:700;font-size:10px;padding:5px 12px;border-radius:2px;color:#fff}

/* services */
.service{top:369px;width:170px}
.service .icon{width:30px;height:30px;border-radius:50%;background:var(--slate);position:absolute;left:0;top:0;display:flex;align-items:center;justify-content:center}
.service h3{position:absolute;left:38px;top:7px;font-size:10.5px;font-weight:700;color:var(--teal);white-space:nowrap}
.service .sub{position:absolute;left:38px;top:22px;font-size:6px;color:var(--muted)}
.service p{position:absolute;left:0;top:39px;font-size:6.6px;line-height:1.6;color:#555;width:170px}
.service a{color:var(--blue);text-decoration:none}

/* dark band */
.dark-band{left:0;top:488px;width:769px;height:234px}
.section-title{font-family:"PT Sans",Arial,sans-serif;font-size:12px;color:#fff;display:flex;align-items:center;gap:8px}
.section-title::after{content:"";flex:1;height:5px;background:repeating-linear-gradient(135deg,#333 0 1px,transparent 1px 3px)}
.who{left:106px;top:544px;width:362px;color:#ddd}
.who p{font-size:6.6px;line-height:1.75;margin-top:9px}
.who a{color:var(--gold-bright)}
.testimonials{left:491px;top:544px;width:172px}
.bubble{margin-top:11px;height:84px;background:#2f2f2f;border-radius:12px;padding:10px 16px;color:var(--gold-bright);font-style:italic;font-size:6.6px;line-height:1.7}
.author{margin-top:10px;text-align:center;color:#fff;font-size:6.6px}

/* projects */
.projects-title{left:106px;top:741px;font-size:13px;color:var(--teal)}
.filters{left:454px;top:747px;font-size:6px;color:#666;display:flex;gap:14px}
.filters .on{color:var(--blue)}
.projects-rule{left:106px;top:762px;width:557px;height:1px;background:#ddd}
.thumb{top:775px;width:122px;height:129px;background:#fff;border:3px solid #ddd}
.thumb-label{left:255px;top:876px;width:118px;height:25px;background:var(--blue);color:#fff;font-weight:700;font-size:7px;padding:9px 7px;display:flex;justify-content:space-between;align-items:center}
.thumb-label span{width:13px;height:13px;border-radius:50%;background:#2a5f93;margin-top:-4px}
.arrow-small{top:829px;width:20px;height:20px;border-radius:50%;background:var(--slate);display:flex;align-items:center;justify-content:center}

/* footer */
.footer{left:0;top:944px;width:769px;height:228px;background:var(--night);border-top:2px solid var(--blue)}
.footer .section-title{font-size:11px}
.footer .section-title::after{display:none}
.col-line{height:2px;background:#333;margin-top:8px}
.blog{left:106px;top:974px;width:172px}
.post{display:flex;gap:7px;height:47px;border-bottom:1px solid #2c2c2c;padding-top:6px}
.post .ph{width:36px;height:35px;background:#3a3a3a;border-radius:2px;flex:none}
.post p{font-size:6.6px;color:#bbb;line-height:1.5}
.post small{display:block;font-size:5.5px;color:#777;margin-top:3px;font-style:italic}
.visit{margin-top:14px;font-size:6px;color:var(--gold-bright);text-decoration:underline}
.agents{left:298px;top:974px;width:176px}
.agents p{font-size:6.5px;color:#555;line-height:1.6;margin-top:9px}
.field{margin-top:10px;height:23px;background:#888;border:1px solid #aaa;color:#ddd;font-size:8px;padding:6px 8px}
.btn-gold{display:inline-block;margin-top:10px;background:var(--gold);color:#333;font-family:"PT Sans",Arial,sans-serif;font-size:8.5px;padding:5px 10px}
.contact{left:491px;top:974px;width:172px}
.contact li{list-style:none;display:flex;gap:12px;font-size:6.2px;color:#777;line-height:1.5;margin-top:9px;align-items:flex-start}
.contact svg{flex:none;margin-top:1px}
.touch{margin:18px 0 0 28px;width:112px;height:21px;background:var(--gold);color:#333;font-family:"PT Sans",Arial,sans-serif;font-size:9px;display:flex;align-items:center;justify-content:center;gap:6px}
.bottombar{left:0;top:1172px;width:769px;height:28px;background:#0d0d0d;color:#666;font-size:6px;padding:11px 106px;display:flex;justify-content:space-between}
.bottombar b{font-weight:400;display:flex;align-items:center;gap:5px}
.bottombar i{width:9px;height:9px;border-radius:50%;background:var(--gold-bright)}
</style>
</head>
<body>

<div class="abs topbar">E-mail: <a href="#">hello@corvane.ca</a> &nbsp;|&nbsp; Mobile: <span style="color:#3a6fa0">514 555 019</span></div>
<div class="abs social" aria-label="Social links"><span></span><span></span><span></span><span></span><span></span></div>

<div class="abs brand"><span class="brand-name">Corvane</span><span class="brand-mark"></span></div>
<div class="abs brand-tag">Web Solutions</div>

<nav class="abs nav">
  <a class="current" href="#">Home</a><a href="#">About Us</a><a href="#">Portfolio</a><a class="open" href="#">Blog</a><a href="#">Contact</a>
</nav>

<div class="abs rule" style="top:84px"></div>
<div class="abs slider-band"></div>
<div class="abs slide-image" role="img" aria-label="Slider photo showcasing a web design project"></div>
<div class="abs arrow-big left"><svg width="12" height="14"><path d="M9 1 3 7l6 6" stroke="#fff" stroke-width="3" fill="none"/></svg></div>
<div class="abs arrow-big right"><svg width="12" height="14"><path d="M3 1l6 6-6 6" stroke="#fff" stroke-width="3" fill="none"/></svg></div>
<div class="abs caption">
  <h2>WE MAKE THE WEB AMAZING</h2>
  <p>Duo probo dicunt efficiendi in, cu vim graecis invidunt, nemore patrioque pri id. Mei aliquip menandri ea. Ex pri dictas petentium constituto, cum cu facilis blandit. Dicat summo duo ea, ex sed assum delicatissimi has.</p>
  <div class="cta"><span class="btn-blue">TAKE A TOUR</span> or <span class="btn-blue">GET A QUOTE</span></div>
</div>

<ul class="abs dropdown">
  <li>Our History</li><li class="active">Company Mission</li><li>Team</li><li>Clients Testimonials</li>
</ul>
<div class="abs rule" style="top:56px;left:578px;width:80px"></div>

<div class="abs rule" style="top:334px"></div>

<section class="abs service" style="left:106px">
  <div class="icon"><svg width="12" height="16"><path d="M7 0 1 9h4l-1 7 7-10H7z" fill="#fff"/></svg></div>
  <h3>Search Engine Marketing</h3><div class="sub">Graeci lines mollis ne eos in.</div>
  <p>Ex pri dictas petentium constituto, cum cu facilis blandit. Dicat summo duo ea, ex sed assum delicatis-simi. Has pertinax pericula accommodare ei, diam facer deterruisset eum et.</p>
</section>
<section class="abs service" style="left:299px">
  <div class="icon"><svg width="14" height="12"><rect x=".5" y=".5" width="13" height="11" fill="none" stroke="#fff"/><path d="M3 4l2 2-2 2" stroke="#fff" fill="none"/></svg></div>
  <h3>Web Development</h3><div class="sub">Graeci lines mollis ne eos in.</div>
  <p>Ex pri dictas petentium constituto, cum cu facilis blandit. <a href="#">Dicat summo duo</a> ea, ex sed assum delicatis-simi. Has pertinax pericula accommodare ei, diam facer deterruisset eum et.</p>
</section>
<section class="abs service" style="left:491px">
  <div class="icon"><svg width="10" height="14"><circle cx="5" cy="5" r="4" fill="none" stroke="#fff" stroke-width="1.3"/><path d="M3 11h4M3.5 13h3" stroke="#fff"/></svg></div>
  <h3>Social Media Marketing</h3><div class="sub">Graeci lines mollis ne eos in.</div>
  <p>Ex pri dictas petentium constituto, cum cu facilis blandit. Dicat summo duo ea, ex sed assum delicatis-simi. Has pertinax pericula <a href="#">accommodare ei</a>, diam facer deterruisset eum et.</p>
</section>

<svg class="abs dark-band" viewBox="0 0 769 234" aria-hidden="true">
  <path d="M0 2Q384 30 769 2V232Q384 202 0 232Z" fill="var(--night)"/>
  <path d="M0 2Q384 30 769 2" stroke="var(--blue)" stroke-width="2" fill="none"/>
  <path d="M0 232Q384 202 769 232" stroke="var(--blue)" stroke-width="2" fill="none"/>
</svg>

<section class="abs who">
  <h2 class="section-title">Who we are</h2>
  <p>Mel an zril facete option, id his graece <a href="#">atomorum repudiandae</a>, nam an illum ullum graecis. Qui prima desiseu est tota eligendi tractatos ea. Vix nemore invenire gubergren cu. Ne his prompta fabellas, hincts modus eripuit eam et, iusto mucius pertinax ut qui. Zril commune luptatum ex sea. Ius ex putent aliquamse accommodare, at vis semper labitur equidem, pri eius etiam incorrupte cu. Ei vix elit definitiones utamur.</p>
  <p>Duo probo dicunt efficiendi in, cu vim graecis invidunt, nemore patrioque pri id. Mei aliquip menandri ea. Ex pri dictas petentium constituto, cum cu facilis blandit. Dicat summo duo ea, ex sed assum delicatissimi has.</p>
</section>
<section class="abs testimonials">
  <h2 class="section-title">Testimonials</h2>
  <div class="bubble">Vestibulum accumsan tristique massa, ac aliquam augue volutpat eget. Donec justo eros, gravida tristique ornare sit amet, rhon-cus a leo. Nulla facilisi. Integer rutrum nisl eros.</div>
  <div class="author">Marten Vale, <b>Norvel Company</b></div>
</section>

<h2 class="abs projects-title">Latest Projects</h2>
<div class="abs filters"><span class="on">All Projects</span><span>Web Design</span><span>Logo Design</span><span>SEO</span><span>Illustrations</span></div>
<div class="abs projects-rule"></div>
<div class="abs arrow-small" style="left:74px"><svg width="6" height="8"><path d="M5 1 2 4l3 3" stroke="#fff" stroke-width="1.5" fill="none"/></svg></div>
<div class="abs thumb" style="left:109px" role="img" aria-label="Portfolio project preview"></div>
<div class="abs thumb" style="left:252px" role="img" aria-label="Portfolio project preview"></div>
<div class="abs thumb" style="left:395px" role="img" aria-label="Portfolio project preview"></div>
<div class="abs thumb" style="left:537px" role="img" aria-label="Portfolio project preview"></div>
<div class="abs thumb-label">Halden Interactive<span></span></div>
<div class="abs arrow-small" style="left:675px"><svg width="6" height="8"><path d="M1 1l3 3-3 3" stroke="#fff" stroke-width="1.5" fill="none"/></svg></div>

<footer class="abs footer"></footer>
<section class="abs blog">
  <h2 class="section-title">From the Blog</h2><div class="col-line"></div>
  <div class="post"><div class="ph"></div><p>Vivamus mauris justo, fermentum quis mattis vel, auctor vitae metus.<small>22 January 2012 &nbsp;&nbsp; Tutorials</small></p></div>
  <div class="post"><div class="ph"></div><p>Vivamus mauris justo, fermentum quis mattis vel, auctor vitae metus.<small>22 January 2012 &nbsp;&nbsp; Inspiration</small></p></div>
  <div class="post"><div class="ph"></div><p>Vivamus mauris justo, fermentum quis mattis vel, auctor vitae metus.<small>22 January 2012 &nbsp;&nbsp; Web Design</small></p></div>
  <div class="visit">Visit Our Blog</div>
</section>
<section class="abs agents">
  <h2 class="section-title">Remote Agents</h2><div class="col-line"></div>
  <p>Lorem ipsum dolor sit amet, consectetuer adipiscing elit sed diam nonummy nibh euismod tincidunt</p>
  <div class="field">Email Address...</div>
  <span class="btn-gold">SUBSCRIBE NOW</span>
</section>
<section class="abs contact">
  <h2 class="section-title">Contact Us</h2><div class="col-line"></div>
  <ul>
    <li><svg width="7" height="10"><path d="M3.5 0A3.5 3.5 0 0 0 0 3.5C0 6 3.5 10 3.5 10S7 6 7 3.5A3.5 3.5 0 0 0 3.5 0z" fill="#888"/></svg><span>42 Larkspur Avenue, Suite 12<br>Montreal H2X 1Y4, Canada</span></li>
    <li><svg width="7" height="10"><rect x=".5" y=".5" width="6" height="9" rx="1" fill="none" stroke="#888"/></svg><span>+1 (514) 555 0142</span></li>
    <li><svg width="9" height="7"><rect x=".5" y=".5" width="8" height="6" fill="none" stroke="#888"/><path d="M.5.5 4.5 4l4-3.5" stroke="#888" fill="none"/></svg><span>contact@corvane.ca</span></li>
  </ul>
  <div class="col-line" style="margin-top:10px;height:1px"></div>
  <div class="touch"><svg width="9" height="7"><rect width="9" height="7" fill="#333"/><path d="M0 0l4.5 4L9 0" stroke="var(--gold)" fill="none"/></svg>Get in touch today</div>
  <div class="col-line" style="margin-top:10px"></div>
</section>
<div class="abs bottombar"><span>Copyright © 2013. Corvane PVT. LTD. All Right Reserve.</span><b>Back To Top <i></i></b></div>

</body>
</html>
```